Buchcover-Design für Erziehungsratgeber
Zielgruppe
Es handelt sich um einen Erziehungsratgeber zum Thema 'bedürfnisorientierte Erziehung'.
Zielgruppe :
Frauen 25-35 Jahre
Werdende Mütter bzw. Mütter eines Neugeborenen
Personen mit Vorliebe für natürliche Heilmittel, Methoden oder Konzepte.
Personen, die eher Vorbehalte ggü. chemischen, kommerziellen oder industriellen Heilmitteln, Methoden, Konzepten haben.
Aufgabenstellung
Das Cover soll ein Baby 1-12 Monate zeigen, ggf. auch mit der Mutter zusammen.
Das Cover soll Schutz, Geborgenheit und Fürsorge ausstrahlen.
Eine kreativere Titel-Anordnung ist gewünscht. Bitte wählen Sie für die Titel-Anordnung KEINE Standard-Anordnung, also z.B. nicht mittig zentriert im oberen Drittel.
Farbvorschlag für den Titel-Text: 800080ff (abweichende Ideen sind trotzdem gern gesehen)
Stockmaterial wird von Bildtruhenarchiv.com bevorzugt.
Cover-Maße: 6x9 Zoll, 170 Seiten. Bitte Template benutzen.
Das Verlagslogo soll unten Links auf dem Cover abgedruckt werden. Bitte wählen Sie eine zum Cover passende, unauffällige Farbe.
Titel: 'Achtsames Aufwachsen mit Nähe und Vertrauen im ersten Lebensjahr'
Sub-Titel (unauffällig darstellen): 'So begleiten Sie Ihren Säugling mit Ruhe und Feingefühl durch die ersten Wochen und erkennen, welche Signale er Ihnen sendet. Ein Familienbegleiter für das erste Jahr mit Kind'
Autoren-Name: 'Helga Brink'

```html
<!DOCTYPE html>
<html lang="de">
<head>
<meta charset="utf-8">
<title>Achtsames Aufwachsen – Buchcover</title>
<link href="https://fonts.googleapis.com/css2?family=Quicksand:wght@500&family=Arimo:wght@400;700&display=swap" rel="stylesheet">
<style>
  :root {
    --page-bg: #ffffff;
    --plum-title: #61123d;
    --plum-soft: #8c1f5e;
    --badge: #5a1032;
    --badge-text: #ffffff;
    --ink: #1f1a1c;
    --logo-grey: #8a8486;
    --skin-warm: #e9bfa6;
    --skin-light: #f4d8c6;
    --sheet: #fbf8f6;
  }
  html, body {
    margin: 0;
    width: 848px;
    height: 1200px;
    overflow: hidden;
    background: var(--page-bg);
  }
  .cover {
    position: absolute;
    left: 24px;
    top: 0;
    width: 800px;
    height: 1200px;
    overflow: hidden;
    background: var(--sheet);
    font-family: 'Quicksand', sans-serif;
  }
  .cover-photo {
    position: absolute;
    inset: 0;
    background:
      radial-gradient(ellipse 34% 22% at 22% 14%, var(--skin-warm) 0%, rgba(233,191,166,0.6) 45%, rgba(233,191,166,0) 100%),
      radial-gradient(ellipse 30% 20% at 42% 36%, var(--skin-light) 0%, rgba(244,216,198,0.7) 50%, rgba(244,216,198,0) 100%),
      radial-gradient(ellipse 14% 10% at 76% 34%, var(--skin-light) 0%, rgba(244,216,198,0) 100%),
      radial-gradient(ellipse 22% 30% at 4% 40%, #dcae94 0%, rgba(220,174,148,0) 100%),
      radial-gradient(ellipse 55% 16% at 35% 60%, rgba(240,214,198,0.8) 0%, rgba(240,214,198,0) 100%),
      radial-gradient(ellipse 30% 30% at 2% 80%, rgba(236,206,188,0.8) 0%, rgba(236,206,188,0) 100%),
      linear-gradient(180deg, #f9f3ef 0%, #f6eee9 50%, #faf7f5 100%);
  }
  .author {
    position: absolute;
    right: 53px;
    top: 40px;
    margin: 0;
    font-size: 29px;
    font-weight: 500;
    color: var(--ink);
  }
  .badge {
    position: absolute;
    left: 528px;
    top: 140px;
    width: 176px;
    height: 176px;
    border-radius: 50%;
    background: var(--badge);
    color: var(--badge-text);
    font-family: 'Arimo', sans-serif;
    font-size: 17px;
    line-height: 1.3;
    display: flex;
    align-items: center;
    justify-content: center;
    text-align: center;
    padding: 0 26px;
    box-sizing: border-box;
    transform: rotate(-6deg);
  }
  .title {
    position: absolute;
    left: 54px;
    top: 600px;
    width: 700px;
    margin: 0;
    font-weight: 500;
    line-height: 1;
  }
  .title span { display: block; white-space: nowrap; }
  .title-small { color: var(--plum-soft); font-size: 46px; }
  .title-big { color: var(--plum-title); font-size: 104px; letter-spacing: -2px; }
  .title-line-2 { margin-top: 6px; }
  .title-line-3 { font-size: 42px; margin-top: 22px; }
  .title-line-4 { margin-left: 130px; margin-top: 8px; }
  .publisher {
    position: absolute;
    left: 61px;
    top: 1080px;
    font-family: 'Arimo', sans-serif;
    font-weight: 700;
    font-size: 20px;
    line-height: 1.05;
    color: var(--logo-grey);
  }
  .subtitle {
    position: absolute;
    left: 189px;
    top: 1098px;
    width: 560px;
    margin: 0;
    font-family: 'Arimo', sans-serif;
    font-size: 16px;
    line-height: 1.45;
    color: var(--ink);
  }
</style>
</head>
<body>
  <main class="cover">
    <div class="cover-photo" role="img" aria-label="Foto: schlafende Mutter hält ihr schlafendes Baby in weißer Bettwäsche"></div>
    <p class="author">Helga Brink</p>
    <div class="badge">Ein Familienbegleiter für das erste Jahr mit Kind</div>
    <h1 class="title">
      <span class="title-small title-line-1">Achtsames Aufwachsen</span>
      <span class="title-big title-line-2">mit Nähe</span>
      <span class="title-small title-line-3">und Vertrauen im ersten</span>
      <span class="title-big title-line-4">Lebensjahr</span>
    </h1>
    <div class="publisher">Lindwerk<br>Verlag</div>
    <p class="subtitle">So begleiten Sie Ihren Säugling mit Ruhe und Feingefühl durch die ersten Wochen und erkennen, welche Signale er Ihnen sendet.</p>
  </main>
</body>
</html>
```